Uplift: Covid 19 (Poster)

We are looking to create a 11 by 17 inch 1 page poster.
-- Please Include NKR’s logo
-- Use the colors and font and mimic the feel of from Steady Step, Steady Breath Resource - Dementia Risk Reduction Flyers - Northern Council for Tribal Longevity (nkrcircle.org)
--> https://nkrcircle.org/resource-dementia-risk-reduction-flyers/
Moto needs to be included and it is: Protect Your Community. Protect Your Elders. Stay Vaccinated.
Include funding statement at the bottom of document - small print:
This project is supported by the Bureau for Illness Monitoring and Response of the U.S. Office of Wellness and Family Programs (OWFP) as part of a financial assistance award totaling $20,007,444 with 100 percent funded by BIMR/OWFP. The contents are those of the author(s) and do not necessarily represent the official views of, nor an endorsement, by BIMR/OWFP, or the U.S. Government.

```html
<!DOCTYPE html>
<html lang="en">
<head>
<meta charset="utf-8">
<title>Uplift – COVID-19 Poster</title>
<link rel="stylesheet" href="https://fonts.googleapis.com/css2?family=Bebas+Neue&family=Open+Sans:wght@400;700&display=swap">
<style>
  :root{
    --paper:#efe5d6;
    --paper-deep:#e6d9c5;
    --brick:#b4544f;
    --brick-dark:#7a3531;
    --teal:#3c9fab;
    --band-teal:#5f9a9c;
    --band-red:#a9554c;
    --photo-warm:#c79a6e;
    --photo-violet:#8e3b86;
  }
  *{box-sizing:border-box;margin:0;padding:0}
  html,body{width:776px;height:1200px;overflow:hidden;background:var(--paper)}
  .poster{position:relative;width:776px;height:1200px;overflow:hidden;
    background:linear-gradient(180deg,var(--paper) 0%,var(--paper-deep) 100%);
    font-family:"Open Sans",Arial,sans-serif}
  .band{position:absolute;left:0;width:100%;height:36px;
    background:linear-gradient(180deg,var(--band-teal) 0 40%,var(--band-red) 40% 60%,var(--band-teal) 60% 100%)}
  .band--top{top:0}
  .band--bottom{bottom:0}
  .title{position:absolute;top:46px;left:0;width:100%;text-align:center;
    font-family:"Bebas Neue",Impact,sans-serif;font-size:122px;line-height:1;color:var(--brick);letter-spacing:1px}
  .motto{position:absolute;top:170px;left:0;width:100%;text-align:center;
    font-family:"Bebas Neue",Impact,sans-serif;font-size:35px;line-height:1.05;color:var(--teal);letter-spacing:.5px}
  .lead{position:absolute;left:33px;width:740px;color:var(--brick);font-weight:700;font-size:20.5px;line-height:1.32;white-space:nowrap}
  .lead--risk{top:263px}
  .lead--symptoms{top:484px}
  .checks{position:absolute;left:45px;list-style:none;color:var(--teal);font-size:18.5px}
  .checks li{position:relative;padding-left:18px}
  .checks li::before{content:"";position:absolute;left:0;top:5px;width:7px;height:12px;
    border:solid var(--teal);border-width:0 3px 3px 0;transform:rotate(40deg)}
  .checks--facts{top:358px;width:500px;line-height:1.55}
  .checks--symptoms{top:590px;line-height:29.3px}
  .photo{position:absolute;right:0;top:340px;width:520px;height:824px;
    background:radial-gradient(ellipse at 75% 35%,var(--photo-violet) 0%,var(--photo-warm) 45%,rgba(239,229,214,0) 75%);}
  .partner{position:absolute;left:17px;top:990px;display:flex;align-items:center;gap:12px;
    color:var(--teal);font-weight:700;font-size:15px;line-height:1.15;width:300px}
  .partner__mark{width:70px;height:70px;border-radius:50%;background:var(--teal);flex:none}
  .funder{position:absolute;left:17px;top:1074px;display:flex;align-items:center;gap:14px;
    color:var(--brick);font-weight:700;font-size:20px;line-height:1.15;width:420px}
  .funder__mark{width:70px;height:56px;background:var(--teal);flex:none}
  .funding-note{position:absolute;left:17px;top:1137px;width:742px;
    color:var(--brick-dark);font-size:7.4px;line-height:9px}
</style>
</head>
<body>
<main class="poster">
  <div class="band band--top"></div>

  <h1 class="title">UPLIFT</h1>
  <p class="motto">Protect your community. Protect your elders.<br>Stay vaccinated. Fight COVID-19!</p>

  <p class="lead lead--risk">American Indian and Alaska Native people have a higher risk<br>of COVID-19 infection rate than other population<br>in the United States.</p>

  <div class="photo" role="img" aria-label="Photograph of two Native elder women in traditional dress with turquoise jewelry and a woven blanket"></div>

  <ul class="checks checks--facts">
    <li>COVID-19 is a virus that spreads mainly when<br>infected people cough, sneeze, or talk.</li>
    <li>The best way to prevent yourself and others from<br>COVID-19 is by staying up to date with vaccination</li>
  </ul>

  <p class="lead lead--symptoms">COVID-19 symptoms may take 2 to 14 days<br>to appear after exposure to the virus,<br>and symptoms may include:2</p>

  <ul class="checks checks--symptoms">
    <li>Fever or chills</li>
    <li>Cough</li>
    <li>Shortness of breath or difficulty</li>
    <li>breathing</li>
    <li>Fatigue</li>
    <li>Muscle or body aches</li>
    <li>Headache</li>
    <li>New loss of taste or smell</li>
    <li>Sore throat</li>
    <li>Congestion or runny nose</li>
    <li>Nausea or vomiting</li>
    <li>Diarrhea</li>
  </ul>

  <div class="partner">
    <span class="partner__mark"></span>
    <span>TRIBAL WELLNESS RESOURCE CENTER FOR BRAIN HEALTH</span>
  </div>

  <div class="funder">
    <span class="funder__mark"></span>
    <span>NORTHERN COUNCIL FOR TRIBAL LONGEVITY</span>
  </div>

  <p class="funding-note">This project is supported by the Bureau for Illness Monitoring and Response of the U.S. Office of Wellness and Family Programs (OWFP) as part of a financial assistance award totaling $20,007,444 with 100 percent funded by BIMR/OWFP. The contents are those of the author(s) and do not necessarily represent the official views of, nor an endorsement, by BIMR/OWFP, or the U.S. Government.</p>

  <div class="band band--bottom"></div>
</main>
</body>
</html>
```